New Innovative Counselling and psychotherapy Service needs Business Card design

Keep it simple and professional. On one side, just company name and logo (perhaps in all blue) and maybe a tag line.

On other side (all white) my name and Qualifications in centre

Industry/Entity Type

Health And Wellness

Contact Information for Business Card

Derek Hollis
Counsellor & Psychotherapist
BSc (Psychol.), BA, Dip. (Couns. & Psych.), PG.Cert (CBT), MGVrA, NWTF

I will also require Mobile no, Email and web site address of which I'll pass on to final designer.

Font styles to use
Sans Serif

Requirements
Must have
• My Logo Only and please use the colours in logo that is in it.
Should not have
• Any other images

```html
<!DOCTYPE html>
<html lang="en">
<head>
<meta charset="UTF-8">
<title>Elmstead Counselling Business Cards</title>
<link rel="stylesheet" href="https://fonts.googleapis.com/css2?family=Montserrat:wght@400;500;600&display=swap">
<style>
  :root {
    --backdrop: #2a2a2b;
    --card: #1c1c1d;
    --ink: #f2f2f2;
    --ink-soft: #e0e0e0;
    --blue: #3aa6e0;
    --green: #7cc242;
    --silver: #c4c4c4;
  }
  * { margin: 0; padding: 0; box-sizing: border-box; }
  html, body {
    width: 1200px; height: 900px; overflow: hidden;
    background: var(--backdrop);
    font-family: "Montserrat", sans-serif;
    color: var(--ink);
  }
  .canvas {
    position: relative; width: 1200px; height: 900px;
    display: flex; flex-direction: column; align-items: center;
    justify-content: center; gap: 40px;
  }
  .card {
    position: relative; width: 700px; height: 400px;
    background: var(--card);
    border-radius: 3px;
  }
  /* Back side */
  .card--back {
    display: flex; flex-direction: column; align-items: center; justify-content: center;
  }
  .back-brand {
    font-size: 40px; font-weight: 500; color: var(--silver);
    letter-spacing: 1px; margin-top: -20px;
  }
  .back-web {
    position: absolute; bottom: 52px; left: 0; right: 0; text-align: center;
    font-size: 16px; letter-spacing: 0.5px; color: var(--ink);
  }
  .back-web .accent { color: var(--green); }
  /* Front side */
  .card--front { display: flex; align-items: center; }
  .front-brand {
    width: 330px; padding-left: 52px;
    font-size: 26px; font-weight: 400; color: var(--ink);
    letter-spacing: 0.5px; line-height: 1.25;
  }
  .divider {
    width: 3px; height: 200px; background: var(--green); margin: 0 24px 0 10px;
  }
  .details { display: flex; flex-direction: column; }
  .person-name {
    font-size: 32px; font-weight: 600; color: var(--blue); letter-spacing: 0.5px;
    line-height: 1.05; margin-bottom: 2px;
  }
  .person-role, .qualifications {
    font-size: 16px; font-weight: 500; color: var(--ink-soft); line-height: 1.35;
  }
  .qualifications { margin-bottom: 12px; }
  .contact-list { list-style: none; }
  .contact-item {
    display: flex; align-items: center; gap: 12px;
    font-size: 17px; color: var(--ink); line-height: 1.55;
  }
  .contact-item svg { width: 13px; height: 13px; flex: none; }
  .contact-item .accent { color: var(--green); }
</style>
</head>
<body>
<main class="canvas">
  <section class="card card--back" aria-label="Business card back">
    <p class="back-brand">Elmstead Counselling</p>
    <p class="back-web">www.<span class="accent">elmstead</span>.com</p>
  </section>

  <section class="card card--front" aria-label="Business card front">
    <p class="front-brand">Elmstead<br>Counselling</p>
    <div class="divider"></div>
    <div class="details">
      <h1 class="person-name">DEREK HOLLIS</h1>
      <p class="person-role">Counsellor &amp; Psychotherapist</p>
      <p class="qualifications">BSc (Psychol.), BA, Dip.<br>(Couns. &amp; Psych.), PG.Cert<br>(CBT), MGVrA, NWTF</p>
      <ul class="contact-list">
        <li class="contact-item">
          <svg viewBox="0 0 16 16" aria-hidden="true"><path d="M4 1l3 3-1.5 2a9 9 0 0 0 4.5 4.5L12 9l3 3-2 3C7 15 1 9 1 3z" fill="var(--blue)"/></svg>
          555-014-2271
        </li>
        <li class="contact-item">
          <svg viewBox="0 0 16 16" aria-hidden="true"><rect x="1.5" y="3.5" width="13" height="9" fill="none" stroke="var(--blue)" stroke-width="1.5"/><path d="M1.5 3.5l6.5 5 6.5-5" fill="none" stroke="var(--blue)" stroke-width="1.5"/></svg>
          info@elmstead.com
        </li>
        <li class="contact-item">
          <svg viewBox="0 0 16 16" aria-hidden="true"><g fill="none" stroke="var(--blue)" stroke-width="1.3"><circle cx="8" cy="8" r="6.5"/><ellipse cx="8" cy="8" rx="3" ry="6.5"/><path d="M1.5 8h13M2.5 4.8h11M2.5 11.2h11"/></g></svg>
          <span>www.<span class="accent">elmstead</span>.com</span>
        </li>
      </ul>
    </div>
  </section>
</main>
</body>
</html>
```